Health & Fitness Author & Public Speaker Needs Visually Stunning Web Redesign!

It's time for a redesign of the home page for Beatrix Holloway's "Bright Fork Kitchen" website (www.brightforkkitchen.example). We have a VERY clear idea of what we want, so it really won't take a talented designer long to bring it to life.
The website itself is used to promote & sell her range of health & nutrition programs to a female audience, primarily aged 24 - 35 working in professional or semi professional occupations.
For a VERY comprehensive outline of exactly what we are after, please see the following attached files:
(1) 'Website - WireFrame' (layout, content/copy, visual design style we want along with the desired color scheme)
(2) 'Website - Style Guide' (these are the colours, and overall feel we want)
PLEASE REVIEW THIS IN FULL - THEY WILL GIVE YOU A VERY CLEAR IDEA OF WHAT WE WANT.
Most of the files you need are attached, but for more photos that you can use (of Beatrix, her programs, and food/meals) can be found at these URL's:
BEATRIX (profile photos):
https://www.filevault.example/s/k3m9p2x7q1/AbCdEf1234
ECOVERS
- Bright Fork Kitchen Guide (ebook): https://www.filevault.example/s/r8t4w6y2n5/GhIjKl5678
- 6 Week Total Momentum Course (ecourse): https://www.filevault.example/s/u1v5z9c3b7/MnOpQr9012
- E-Magazine Issues:
https://www.filevault.example/s/d2f6h8j4l0/StUvWx3456
STOCK IMAGES:
https://www.filevault.example/s/g7k1m5n9p3/YzAbCd7890
As we will need to revamp our existing Circlebook page & other printed material, there may be the potential for further work for the successful designer in the future.
Thanks & Good Luck!
Desmond Farrow
Marketing & Business Development Manager
Bright Fork Kitchen

```html
<!DOCTYPE html>
<html lang="en">
<head>
<meta charset="utf-8">
<title>Bright Fork Kitchen – Home</title>
<link href="https://fonts.googleapis.com/css2?family=Open+Sans:ital,wght@0,400;0,600;0,700;1,700&family=Oswald:wght@400;500&display=swap" rel="stylesheet">
<style>
:root{
  --navy:#2a3850;
  --navy-dark:#1f2a3d;
  --pink:#e8175d;
  --pink-dark:#c4124d;
  --teal:#2ebdb7;
  --teal-dark:#239d98;
  --ink:#333;
  --grey:#7a7a7a;
  --line:#d9d9d9;
  --band:#333333;
  --paper:#ffffff;
  --soft:#f2f2f2;
}
*{box-sizing:border-box;margin:0;padding:0}
html,body{width:1200px;height:2456px;overflow:hidden}
body{position:relative;background:var(--paper);font-family:"Open Sans",Arial,sans-serif;color:var(--ink)}
.abs{position:absolute}

/* hero */
.hero{left:0;top:0;width:1200px;height:475px;background:linear-gradient(90deg,var(--navy-dark),var(--navy) 40%,var(--navy))}
.site-header{left:115px;top:16px;width:970px;height:85px;background:var(--paper);border-bottom:4px solid var(--pink);display:flex;align-items:center;justify-content:space-between;padding-left:20px}
.brand{display:flex;align-items:center;gap:10px;font-weight:700;font-size:24px;color:var(--pink)}
.brand-dot{width:14px;height:14px;border-radius:50%;background:var(--pink)}
.main-nav{display:flex;height:100%;align-items:flex-end}
.main-nav a{display:block;padding:0 20px;height:34px;line-height:34px;font-size:13px;color:var(--ink);text-decoration:none;text-transform:uppercase}
.main-nav a.active{background:var(--pink);color:#fff;font-weight:600}
.hero-banner{left:115px;width:425px;height:56px;background:var(--teal);color:#fff;font-family:"Oswald",sans-serif;font-weight:500;font-size:34px;text-align:center;line-height:56px;box-shadow:0 6px 6px -3px rgba(0,0,0,.35)}
.hero-photo{left:715px;top:101px;width:175px;height:374px;background:linear-gradient(180deg,#c9bfb6,#e6e0dc 45%,#20232a 70%,#1a1c22);border-radius:60px 60px 0 0}

/* signup strip */
.signup-strip{left:0;top:475px;width:1200px;height:82px;background:var(--pink);box-shadow:0 8px 10px -6px rgba(0,0,0,.35)}
.strip-title{left:115px;top:10px;color:#fff;font-weight:700;font-style:italic;font-size:17px}
.strip-copy{left:115px;top:36px;width:300px;color:#fff;font-size:10.5px;font-weight:600;line-height:1.35}
.mail-icon{left:458px;top:18px;width:44px;height:44px;border:2px solid rgba(255,255,255,.7);border-radius:50%}
.strip-input{top:26px;width:203px;height:28px;background:var(--pink-dark);color:#f6c5d6;font-size:11px;line-height:28px;padding-left:10px}
.strip-button{left:982px;top:26px;width:103px;height:28px;background:var(--teal);color:#10343a;font-size:13px;font-weight:600;text-align:center;line-height:28px}

/* main column */
.content{left:115px;top:586px;width:643px}
.section-title{color:var(--pink);font-weight:700;font-size:17.5px;line-height:1.35}
.body-copy{color:var(--grey);font-size:11.5px;line-height:1.75}
.plus-list{list-style:none}
.plus-list li{position:relative;padding-left:25px;font-size:11.5px;color:var(--ink);height:29px;line-height:16px}
.plus-list li.two-line{height:40px}
.plus-list li::before{content:"+";position:absolute;left:0;top:-2px;font-size:17px;color:var(--grey)}
.rule{border:0;border-top:2px solid var(--line)}
.video{position:absolute;width:303px;height:228px;background:#2b2b2b;overflow:hidden}
.video-frame{position:absolute;left:0;top:0;width:100%;height:196px}
.video-bar{position:absolute;left:0;bottom:0;width:100%;height:32px;background:#1b1b1b;color:#ccc;font-size:9px}
.video-bar .track{position:absolute;left:0;top:0;width:100%;height:4px;background:#555}
.video-bar .played{position:absolute;left:0;top:0;width:48%;height:4px;background:#d42525}
.video-bar .time{position:absolute;left:58px;top:13px}
.highlight{color:var(--pink);font-weight:700;font-size:17px;line-height:1.4}

/* sidebar */
.sidebar-box{left:804px;width:271px;box-shadow:0 6px 8px -4px rgba(0,0,0,.35)}
.search-box{top:589px;height:90px;background:var(--soft);padding:12px 18px}
.search-title{color:var(--pink);font-weight:700;font-size:15px}
.search-field{margin-top:10px;display:flex;height:28px}
.search-field span{flex:1;background:#fff;border:1px solid var(--line);font-size:10px;color:#999;line-height:26px;padding-left:8px}
.search-field i{width:30px;background:var(--teal)}
.promo-photo{top:707px;height:275px;background:linear-gradient(160deg,#7fae4a,#a9cc6f 55%,#ddd)}
.kick-badge{left:10px;top:140px;width:140px;height:140px;border-radius:50%;background:rgba(40,40,40,.85);color:#fff;text-align:center;padding-top:28px}
.kick-badge b{display:block;font-family:"Oswald",sans-serif;font-size:19px;line-height:1.15;color:#7fe0d9}
.kick-badge em{display:block;font-size:9px;line-height:1.3;margin-top:6px;padding:0 10px}
.order-box{top:1010px;height:267px;background:linear-gradient(160deg,#b9c7d6,#8ea2b8)}
.order-title{left:14px;top:10px;font-family:"Oswald",sans-serif;font-size:27px;color:var(--pink)}
.order-copy{left:16px;top:58px;width:130px;font-size:11px;color:#222;line-height:1.35}
.order-link{left:16px;top:140px;font-family:"Oswald",sans-serif;font-size:22px;color:#222;text-decoration:underline}
.order-covers{left:14px;top:190px;width:243px;height:70px;background:linear-gradient(90deg,#e8175d,#f3a6c0,#e8175d)}
.emag-box{top:1303px;height:305px;background:linear-gradient(180deg,#8fb5c9,#c9a96a 55%,#2d6d5a)}
.emag-words{left:140px;top:14px;text-align:right;width:118px;font-family:"Oswald",sans-serif;font-style:normal;color:var(--pink);font-size:17px;line-height:1.15}
.emag-big{left:140px;top:85px;width:118px;text-align:right;font-family:"Oswald",sans-serif;color:#fff;font-size:30px}
.emag-foot{left:0;bottom:0;width:100%;height:32px;background:#2c4d3f;color:#9fe26a;font-style:italic;font-weight:700;font-size:14px;text-align:center;line-height:32px}
.social-box{top:1629px;height:229px;background:#fff;border:1px solid #aebbd2}
.social-head{height:24px;background:#4a5f8c;color:#fff;font-size:11px;font-weight:700;text-align:right;line-height:24px;padding-right:10px}
.social-card{padding:10px 12px;font-size:10px;color:#333}
.avatar-grid{display:grid;grid-template-columns:repeat(7,26px);gap:6px 8px;margin-top:8px}
.avatar-grid i{height:26px;background:#c8cbd2}

/* sign-up band */
.join-band{left:0;top:2027px;width:1200px;height:273px;background:var(--band)}
.join-photo{left:123px;top:4px;width:155px;height:269px;background:linear-gradient(180deg,#4a3b35,#6a4d7a 60%,#3c2c45);border-radius:70px 70px 0 0}
.join-title{left:311px;top:12px;color:#fff;font-weight:700;font-size:15.5px;line-height:1.5}
.join-sub{left:311px;top:56px;color:#888;font-size:10px}
.join-label{left:373px;color:#aaa;font-size:10px}
.join-field{left:373px;width:254px;height:26px;border:1px solid #555;background:#3a3a3a}
.join-button{left:373px;top:219px;width:254px;height:28px;background:var(--teal);color:#fff;font-size:11px;text-align:center;line-height:28px}
.join-video{left:707px;top:36px;width:370px;height:237px}

/* partners + footer */
.partners{left:0;top:2300px;width:1200px;height:93px;display:flex;align-items:center;justify-content:space-between;padding:0 125px}
.partner-badge{width:200px;height:38px;background:#e4e4e4;border-radius:4px}
.site-footer{left:0;top:2393px;width:1200px;height:63px;background:var(--pink)}
.footer-nav{left:115px;top:12px;display:flex;gap:18px;font-size:10.5px;color:#fff}
.footer-copy{left:115px;top:36px;font-size:10.5px;color:#fff}
.social-icons{left:842px;top:14px;display:flex;gap:14px}
.social-icons i{width:30px;height:30px;border-radius:50%;background:#fff;opacity:.9;border:3px solid var(--pink-dark)}
</style>
</head>
<body>

<section class="abs hero">
  <header class="abs site-header" style="left:115px;top:16px">
    <div class="brand"><span class="brand-dot"></span>Bright Fork Kitchen</div>
    <nav class="main-nav">
      <a class="active">Home</a><a>About Beatrix</a><a>The Magazine</a><a>Blog &amp; Videos</a><a>Shop</a><a>Contact Us</a>
    </nav>
  </header>
  <div class="abs hero-banner" style="top:169px">YOU DON'T NEED</div>
  <div class="abs hero-banner" style="top:254px">ANOTHER DIET TO GET</div>
  <div class="abs hero-banner" style="top:339px">THE BODY YOU WANT</div>
  <div class="abs hero-photo" role="img" aria-label="Photo of Beatrix standing in a white top holding grapes"></div>
</section>

<section class="abs signup-strip">
  <div class="abs strip-title">Get my FREE monthly E-Magazine</div>
  <div class="abs strip-copy">With delicious recipes,inspirational articles, workouts &amp; expert wellness tips that actually work! Yup FREE!</div>
  <svg class="abs mail-icon" viewBox="0 0 44 44"><rect x="12" y="15" width="20" height="14" fill="none" stroke="#fff" stroke-width="1.6"/><path d="M12 15 L22 23 L32 15" fill="none" stroke="#fff" stroke-width="1.6"/></svg>
  <div class="abs strip-input" style="left:534px">Enter your name :</div>
  <div class="abs strip-input" style="left:753px">Enter your email :</div>
  <div class="abs strip-button">Yes Please!</div>
</section>

<main class="abs content">
  <h2 class="section-title">Want a Body You're Proud Of AND a Healthy Lifestyle You Love? Then You Don't Need Another Diet!</h2>
  <p class="body-copy" style="margin-top:8px">Hey there I'm Beatrix. I help smart, savvy, driven women just like you to slim down so you can not only rock your outfit but you can enjoy a lifestyle to match. As hard as it might be for you to believe right now, I'll teach you how to have this in a way that's easier, and heaps more enjoyable than you'd ever thought possible – it's time to kiss guilt and deprivation goodbye!</p>

  <div style="position:relative;height:250px;margin-top:15px">
    <div class="video" style="left:0;top:0">
      <div class="video-frame" role="img" aria-label="Video still of two women training in a gym" style="background:linear-gradient(135deg,#6b6e78,#a58f8a 50%,#4c4f58)"></div>
      <svg class="abs" style="left:126px;top:72px" width="50" height="50" viewBox="0 0 50 50"><circle cx="25" cy="25" r="24" fill="rgba(0,0,0,.55)"/><path d="M19 14 L37 25 L19 36Z" fill="#fff"/></svg>
      <div class="video-bar"><span class="track"></span><span class="played"></span><span class="time">0:14 / 0:38</span></div>
    </div>
    <div class="video" style="left:330px;top:0">
      <div class="video-frame" role="img" aria-label="Video still of Beatrix holding a slice of watermelon" style="background:linear-gradient(90deg,#5a5a5a,#7a7a7a 60%,#d8d4d0)"></div>
      <svg class="abs" style="left:126px;top:72px" width="50" height="50" viewBox="0 0 50 50"><circle cx="25" cy="25" r="24" fill="rgba(0,0,0,.55)"/><path d="M19 14 L37 25 L19 36Z" fill="#fff"/></svg>
      <div class="video-bar"><span class="track"></span><span class="played"></span><span class="time">0:14 / 0:38</span></div>
    </div>
  </div>

  <h2 class="section-title" style="margin-top:0">Hmmm... do any of these sound familiar?</h2>
  <ul class="plus-list" style="margin-top:14px">
    <li>Tried a bunch of diet plans but you're still stuck in body that just feels yuk</li>
    <li>You "know what to do" but somehow you're still not doing it (WTF!)</li>
    <li>Suffer from emotional eating, feelings of guilt or frustration around food &amp; exercise</li>
    <li>Feel bloated, guilty and maybe even a bit ashamed</li>
    <li>Overwhelmed and frustrated at yourself, feel that being slim and fit is a never ending chore</li>
  </ul>
  <p class="body-copy" style="margin-top:0">You're not the only one... heck that was me at one time. But if you're exhausted at not liking your body, and sick of seeing other women make it all look so easy, don't you think maybe it's time to try something new? Perhaps it's time you stopped following what everyone else is doing (girlfriends, the 19 year old receptionist at work, or that really buffed chick at the gym)... obviously it's not working. So what's the alternative?</p>
  <hr class="rule" style="margin-top:18px">

  <h2 class="section-title" style="margin-top:24px">What If I Told You There Was An Easier &amp; More Enjoyable Way?</h2>
  <ul class="plus-list" style="margin-top:12px">
    <li>To Lose weight (most ladies I work with want to lose between 5kg-10kg... sometimes more)</li>
    <li>Have more energy</li>
    <li>Stop feeling bloated and exhausted</li>
    <li>Stop feeling frustrated for eating the "wrong" things and not exercising "enough"</li>
    <li>Feel hot in your clothes, at work and when you go out</li>
    <li>Feel proud of yourself</li>
    <li>Still have a social life... with you know, friends and stuff!</li>
  </ul>
  <p class="body-copy">Ok... sounds good so far right, but you're probably wondering what is about my method that's so different for all the others out there? Honestly, the problem with most other diet programs is that they:</p>
  <ul class="plus-list" style="margin-top:12px">
    <li>Ignore the importance of pleasure in your life for weight loss. (I think it's key)</li>
    <li>Aren't sustainable- (try and stop me from never eating a French pastry again &amp; see what happens)</li>
    <li>Don't teach you how to never need to be on another program, plan or diet again.</li>
    <li class="two-line">Focus on what you need to cut out (I focus on what you need more of in your life to make it more pleasurable so you can stop feeding the voids in your life with toxic food, booze, etc)</li>
    <li class="two-line">Assume you want the same things as everyone else. They assume your definition of healthy should be the same as everyone else's. (I'll teach you what works for you)</li>
    <li>Ignore the impact that stress has on your ability to shift weight (biochemistry can be cruel).</li>
  </ul>
  <hr class="rule" style="margin-top:4px">
  <p class="body-copy" style="margin-top:14px">I get it. I know and understand first hand your frustrations (I used to be you). <span class="highlight">I know you want it to be effortless. I know you want to not worry about putting on weight EVER, you want to just "Be".</span> You may have some pieces of the puzzle already, but they just never seem to gel together for long enough to get the outcome you truly crave - A hot body you're proud of with a healthy lifestyle you love. I get it. I understand. And I can help you get there.</p>
  <p class="body-copy" style="margin-top:8px">As a qualified Food &amp; Wellness Coach (and Personal Trainer), I've helped thousands of women (starting with myself) just like you over the last 7+ years to not just lose weight (that's nice) but take back control, regain self confidence and find peace with their bodies (that's better – trust me). You can do it to.</p>
  <p class="body-copy" style="margin-top:8px">So what now? First things first, sign up for my E-Magazine below (it's FREE!) to receive some really fantastic recipes, inspirational articles, workouts &amp; expert wellness tips each month.</p>
</main>

<aside>
  <div class="abs sidebar-box search-box">
    <div class="search-title">Search Bright Fork Kitchen</div>
    <div class="search-field"><span>Search</span><i></i></div>
  </div>
  <div class="abs sidebar-box promo-photo" role="img" aria-label="Photo of Beatrix sitting on grass holding an apple">
    <div class="abs kick-badge"><b>6 WEEK TOTAL<br>MOMENTUM</b><em>A complete step by step program to get you on the path to a hotter, healthier &amp; happier you!</em></div>
  </div>
  <div class="abs sidebar-box order-box" role="img" aria-label="Beatrix with watermelon beside Bright Fork Kitchen Guide covers">
    <div class="abs order-title">Order Today</div>
    <div class="abs order-copy">Yours for the awesome price of just $9.95! (Valued $19.95)<br><br>* Limited Time Only</div>
    <div class="abs order-link">★ Buy now</div>
    <div class="abs order-covers"></div>
  </div>
  <div class="abs sidebar-box emag-box" role="img" aria-label="Stack of e-magazine issue covers">
    <div class="abs emag-words">BELIEVE<br>NOURISH<br>RESTORE</div>
    <div class="abs emag-big">E-MAG</div>
    <div class="abs emag-foot">Yours FREE Every Month!</div>
  </div>
  <div class="abs sidebar-box social-box">
    <div class="social-head">Circlebook</div>
    <div class="social-card">
      <div style="color:var(--pink);font-weight:700;font-size:13px">Bright Fork Kitchen</div>
      <div style="margin-top:8px">32,500 people like digital inspiration.</div>
      <div class="avatar-grid"><i></i><i></i><i></i><i></i><i></i><i></i><i></i><i></i><i></i><i></i><i></i><i></i><i></i><i></i></div>
      <div style="margin-top:14px;color:#4a5f8c">Circlebook social plugin</div>
    </div>
  </div>
</aside>

<section class="abs join-band">
  <div class="abs join-photo" role="img" aria-label="Portrait of Beatrix in a purple top"></div>
  <div class="abs join-title">Get Slim, Boost Energy, And<br>Create a Healthy Life You Love!</div>
  <div class="abs join-sub">Join the BRIGHT FORK WELLNESS Revolution!</div>
  <div class="abs join-label" style="top:93px">Enater your name :</div>
  <div class="abs join-field" style="top:110px"></div>
  <div class="abs join-label" style="top:155px">Enater your email :</div>
  <div class="abs join-field" style="top:172px"></div>
  <div class="abs join-button">SING UP ME</div>
  <div class="abs video join-video">
    <div class="video-frame" role="img" aria-label="Video still of Beatrix stretching on a mat" style="height:205px;background:linear-gradient(180deg,#b8b0a6,#d9d2c8 60%,#8b8580)"></div>
    <svg class="abs" style="left:160px;top:78px" width="50" height="50" viewBox="0 0 50 50"><circle cx="25" cy="25" r="24" fill="rgba(0,0,0,.55)"/><path d="M19 14 L37 25 L19 36Z" fill="#fff"/></svg>
    <div class="video-bar"><span class="track"></span><span class="played"></span><span class="time">0:14 / 0:38</span></div>
  </div>
</section>

<section class="abs partners">
  <span class="partner-badge"></span><span class="partner-badge"></span><span class="partner-badge"></span><span class="partner-badge"></span>
</section>

<footer class="abs site-footer">
  <div class="abs footer-nav"><span>Home</span><span>/</span><span>About Beatrix</span><span>/</span><span>The Magazine</span><span>/</span><span>Blog &amp; Videos</span><span>/</span><span>Shop</span><span>/</span><span>Contact Us</span></div>
  <div class="abs footer-copy">Copyright © 2014 brightforkkitchen. All rights reserved</div>
  <div class="abs social-icons"><i></i><i></i><i></i><i></i><i></i><i></i></div>
</footer>

</body>
</html>
```